Australian Recruitment Agency Flyer

We are looking for a 1 page flyer to promote our recruitment company. We would like this to have a corporate look.

Attached is a word document with the content we would like included in the flyer.

I have also attached some of our clients logos to be included in the flyer

Target Market(s)

Professional organisations looking to hire new staff

Industry/Entity Type

It Company

Colors
85abd2
3176b5
31b7a3
d2a4cc
e667a6
b768aa
876aae
3276b5
f04a50

Requirements
Must have
• Must have the content that we have include on a word document in the design brief.

```html
<!DOCTYPE html>
<html lang="en">
<head>
<meta charset="utf-8">
<title>TalentBridge Recruitment Flyer</title>
<link href="https://fonts.googleapis.com/css2?family=Lato:ital,wght@0,400;0,700;0,900;1,400&display=swap" rel="stylesheet">
<style>
  :root {
    --page-bg: #3a3a3c;
    --paper: #ffffff;
    --navy-text: #2b3990;
    --slate: #2c3e50;
    --panel: #2c3d4e;
    --sky: #4fc1e9;
    --blue: #2188cd;
    --deep-blue: #1b64a0;
    --band: #1e88d0;
    --frame-blue: #2f7fc4;
    --ink: #222a33;
    --soft-white: #e8eef3;
  }
  * { margin: 0; padding: 0; box-sizing: border-box; }
  html, body { width: 1200px; height: 1200px; overflow: hidden; }
  body { background: var(--page-bg); font-family: 'Lato', sans-serif; position: relative; }

  .flyer {
    position: absolute; left: 190px; top: 20px;
    width: 980px; height: 1385px;
    background: var(--paper);
    transform: scale(0.8375); transform-origin: top left;
    overflow: hidden;
  }

  .brand { position: absolute; top: 52px; left: 0; width: 100%; display: flex; justify-content: center; align-items: center; gap: 16px; }
  .brand-dot { width: 64px; height: 64px; border-radius: 50%; background: var(--deep-blue); }
  .brand-text { display: flex; flex-direction: column; }
  .brand-name { font-size: 50px; font-weight: 700; color: var(--slate); line-height: 1; letter-spacing: -1px; }
  .brand-tag { font-size: 15px; color: var(--slate); margin-top: 8px; padding-left: 8px; }

  .headline { position: absolute; left: 0; width: 100%; text-align: center; }
  .headline-lead { top: 140px; font-size: 40px; font-weight: 700; color: var(--navy-text); }
  .headline-main { top: 188px; font-size: 42px; font-weight: 900; color: var(--slate); letter-spacing: -0.5px; }

  .testimonial {
    position: absolute; left: 92px; top: 258px; width: 796px; height: 122px;
    border: 2px solid var(--frame-blue); border-radius: 14px;
    text-align: center; color: var(--ink);
  }
  .testimonial-quote { font-style: italic; font-size: 21px; line-height: 28px; margin-top: 10px; }
  .testimonial-quote .mark { font-style: normal; font-weight: 900; font-size: 26px; }
  .testimonial-author { font-size: 20px; margin-top: 8px; }
  .testimonial-author strong { font-weight: 900; font-size: 23px; }

  .team-photo {
    position: absolute; left: 80px; top: 395px; width: 820px; height: 420px;
    background: linear-gradient(180deg, #e9ebee 0%, #c9ccd2 45%, #f4f5f7 100%);
    border-radius: 6px;
  }

  .waves { position: absolute; left: 0; top: 780px; width: 980px; height: 430px; }

  .info { position: absolute; top: 985px; left: 0; width: 980px; height: 220px; color: var(--soft-white); }
  .divider { position: absolute; left: 485px; top: 10px; width: 1px; height: 185px; background: #4a5b6c; }
  .section-head { position: absolute; display: flex; align-items: center; gap: 16px; font-size: 32px; color: var(--sky); font-weight: 400; }
  .section-head svg { width: 38px; height: 38px; }
  .what-head { left: 22px; top: 16px; }
  .industries-head { left: 506px; top: 16px; }
  .what-body { position: absolute; left: 80px; top: 60px; width: 365px; font-size: 17px; line-height: 21px; text-align: justify; }
  .what-body p + p { margin-top: 16px; }
  .industry-list { position: absolute; left: 558px; top: 56px; list-style: none; font-size: 18px; }
  .industry-list li { display: flex; align-items: center; gap: 12px; height: 30px; }
  .industry-list svg { width: 18px; height: 16px; }

  .cta-band { position: absolute; top: 1205px; left: 0; width: 100%; height: 42px; background: var(--band); color: #fff; font-size: 23px; font-weight: 700; text-align: center; line-height: 42px; }

  .clients { position: absolute; top: 1247px; left: 0; width: 100%; height: 90px; display: flex; justify-content: space-around; align-items: center; padding: 0 24px; }
  .client-name { font-size: 20px; font-weight: 700; color: var(--slate); }

  .footer { position: absolute; top: 1337px; left: 0; width: 100%; height: 48px; background: var(--panel); color: #fff; font-size: 22px; letter-spacing: 8px; text-align: center; line-height: 42px; }
</style>
</head>
<body>
  <div class="flyer">
    <header class="brand">
      <div class="brand-dot"></div>
      <div class="brand-text">
        <span class="brand-name">TalentBridge</span>
        <span class="brand-tag">Human Resources &amp; Recruitment</span>
      </div>
    </header>

    <h1 class="headline headline-lead">We have over 20 years of experience</h1>
    <h2 class="headline headline-main">HELPING COMPANIES HIRE AMAZING TALENT</h2>

    <blockquote class="testimonial">
      <p class="testimonial-quote"><span class="mark">&ldquo;</span> TalentBridge really delivered on their promise and far exceeded our expectations.<br>Their fixed fee model saved us thousands <span class="mark">&rdquo;</span></p>
      <p class="testimonial-author"><strong>Mark Ellison General Manager,</strong> Harbour Ridge Financial</p>
    </blockquote>

    <div class="team-photo" role="img" aria-label="Group of business professionals in suits standing together"></div>

    <svg class="waves" viewBox="0 0 980 430" preserveAspectRatio="none" aria-hidden="true">
      <polygon points="0,5 270,63 0,190" fill="#4fc1e9"/>
      <polygon points="390,135 980,17 980,205 500,205" fill="#2188cd"/>
      <polygon points="140,125 270,63 500,205" fill="#1b64a0"/>
      <polygon points="0,190 140,125 500,205 980,205 980,430 0,430" fill="#2c3d4e"/>
    </svg>

    <section class="info">
      <div class="divider"></div>
      <h3 class="section-head what-head">
        <svg viewBox="0 0 38 38"><circle cx="19" cy="19" r="17" fill="none" stroke="#4fc1e9" stroke-width="2"/><circle cx="14" cy="15" r="4" fill="#4fc1e9"/><circle cx="24" cy="15" r="4" fill="#4fc1e9"/><path d="M7 27c1-5 4-7 7-7s6 2 7 7zM17 27c1-5 4-7 7-7s6 2 7 7z" fill="#4fc1e9"/></svg>
        WHAT WE DO
      </h3>
      <div class="what-body">
        <p>We aren't a recruitment agency, we are an extension of your team.</p>
        <p>We become your very own HR &amp; Recruitment department to be called upon as and when needed.</p>
      </div>

      <h3 class="section-head industries-head">
        <svg viewBox="0 0 38 38"><circle cx="19" cy="19" r="17" fill="none" stroke="#4fc1e9" stroke-width="2"/><path d="M8 19l6-4 5 3 5-3 6 4-7 6-4-3-4 3z" fill="#4fc1e9"/></svg>
        INDUSTRIES WE SERVE
      </h3>
      <ul class="industry-list">
        <li><svg viewBox="0 0 18 16"><rect x="1" y="4" width="11" height="11" fill="none" stroke="#e8eef3" stroke-width="1.5"/><path d="M4 9l3 3 9-10" fill="none" stroke="#e8eef3" stroke-width="2"/></svg>Mining and Oil &amp; Gas</li>
        <li><svg viewBox="0 0 18 16"><rect x="1" y="4" width="11" height="11" fill="none" stroke="#e8eef3" stroke-width="1.5"/><path d="M4 9l3 3 9-10" fill="none" stroke="#e8eef3" stroke-width="2"/></svg>Accounting &amp; Finance</li>
        <li><svg viewBox="0 0 18 16"><rect x="1" y="4" width="11" height="11" fill="none" stroke="#e8eef3" stroke-width="1.5"/><path d="M4 9l3 3 9-10" fill="none" stroke="#e8eef3" stroke-width="2"/></svg>Sales &amp; Marketing</li>
        <li><svg viewBox="0 0 18 16"><rect x="1" y="4" width="11" height="11" fill="none" stroke="#e8eef3" stroke-width="1.5"/><path d="M4 9l3 3 9-10" fill="none" stroke="#e8eef3" stroke-width="2"/></svg>IT &amp; Communications</li>
        <li><svg viewBox="0 0 18 16"><rect x="1" y="4" width="11" height="11" fill="none" stroke="#e8eef3" stroke-width="1.5"/><path d="M4 9l3 3 9-10" fill="none" stroke="#e8eef3" stroke-width="2"/></svg>Government &amp; Not for Profit</li>
      </ul>
    </section>

    <div class="cta-band">Start a conversation today and see why these companies turn to us time and time again</div>

    <div class="clients">
      <span class="client-name">Fleetway</span>
      <span class="client-name">Apexa</span>
      <span class="client-name">Redgum Minerals</span>
      <span class="client-name">Kessler Works</span>
      <span class="client-name">Vantix</span>
      <span class="client-name">Harbour Ridge</span>
      <span class="client-name">Quartz Metals</span>
    </div>

    <footer class="footer">www.talentbridge.com.au</footer>
  </div>
</body>
</html>
```